Business Card for Health Food Store

I need a business card for a health food store that includes the following information.

=========
FRONT
=========

***White background***

Fernwick Grove (logo)
Supplements - Health Foods - Remedies

2417 Larkwood Ave.
Calloway Springs, CA 95871
(corner of Dunmore St.)

707-314-2296

GoldenHarvest.example
FernwickLiving@mailbox.example

On the right side of the front of the card, use a circle type seal with 25 large in the middle. Put the dates below it.
"Celebrating 25 Years"
1997 - 2022

*DO NOT USE A PERSON'S NAME ON THE CARD*

==========
BACK
==========

***Green background***

Full logo in white along with the social logos and handles.

FB Logo / FernwickGroveShop
IG Logo / FernwickGroveShop
Twitter Logo / VisitFernwickGrove

When done I'll need the file in PSD and AI.

Target Market(s)

Surrounding local community

Industry/Entity Type

Retail Health Food Store

Contact Information for Business Card

See brief

Requirements
Must have
• Must be double-sided

```html
<!DOCTYPE html>
<html lang="en">
<head>
<meta charset="utf-8">
<title>Fernwick Grove – Business Card</title>
<link rel="stylesheet" href="https://fonts.googleapis.com/css2?family=Outfit:wght@700&family=Figtree:wght@400;600;800&family=Oswald:wght@500&display=swap">
<style>
  :root {
    --backdrop: #d8d8d8;
    --card-white: #ffffff;
    --brand-green: #4db749;
    --ink: #1a1a1a;
    --white: #ffffff;
  }
  * { margin: 0; padding: 0; box-sizing: border-box; }
  html, body { width: 1200px; height: 1059px; overflow: hidden; }
  body { background: var(--backdrop); position: relative; font-family: "Figtree", sans-serif; }

  .card {
    position: absolute; left: 256px; width: 688px; height: 392px;
    border-radius: 18px; overflow: hidden;
  }
  .card--front { top: 100px; background: var(--card-white); }
  .card--back { top: 537px; background: var(--brand-green); }

  .brand { position: absolute; text-align: center; }
  .card--front .brand { left: 46px; width: 278px; top: 128px; }
  .brand__mark { display: block; margin: 0 auto 14px; border-radius: 50%; }
  .card--front .brand__mark { width: 58px; height: 58px; background: var(--brand-green); }
  .brand__name { font-family: "Outfit", sans-serif; font-weight: 700; line-height: 1; white-space: nowrap; letter-spacing: -0.5px; }
  .card--front .brand__name { font-size: 33px; color: var(--ink); }
  .brand__tagline { font-family: "Oswald", sans-serif; font-weight: 500; white-space: nowrap; letter-spacing: 0.6px; }
  .card--front .brand__tagline { font-size: 12.5px; color: var(--brand-green); margin-top: 8px; }

  .divider { position: absolute; left: 334px; top: 119px; width: 1.5px; height: 153px; background: var(--brand-green); }

  .contact { position: absolute; left: 364px; top: 118px; color: var(--ink); font-size: 16px; }
  .contact__address { line-height: 22px; }
  .contact__list { list-style: none; margin-top: 10px; }
  .contact__item { display: flex; align-items: center; gap: 8px; height: 27px; font-size: 15.5px; white-space: nowrap; }
  .contact__icon { width: 14px; height: 14px; flex: none; }

  .seal {
    position: absolute; left: 548px; top: 18px; width: 118px; height: 118px;
    border-radius: 50%; background: var(--brand-green); color: var(--white);
    display: flex; flex-direction: column; align-items: center; justify-content: center;
    text-align: center; line-height: 1;
  }
  .seal__label { font-size: 9px; font-weight: 600; letter-spacing: 1.4px; }
  .seal__number { font-family: "Figtree", sans-serif; font-weight: 800; font-size: 44px; margin: 3px 0 1px; }
  .seal__unit { font-size: 9px; font-weight: 600; letter-spacing: 1.4px; }
  .seal__dates { font-size: 11px; font-weight: 600; margin-top: 6px; padding-top: 5px; border-top: 1px solid rgba(255,255,255,0.7); }

  .card--back .brand { left: 0; right: 0; top: 82px; }
  .card--back .brand__mark { width: 96px; height: 96px; border: 5px solid var(--white); margin-bottom: 28px; }
  .card--back .brand__name { font-size: 48px; color: var(--white); }
  .card--back .brand__tagline { font-size: 20px; color: var(--white); margin-top: 10px; letter-spacing: 0.8px; }

  .socials { position: absolute; left: 0; right: 0; top: 336px; display: flex; justify-content: center; gap: 22px; list-style: none; }
  .socials__item { display: flex; align-items: center; gap: 9px; color: var(--white); font-size: 16px; white-space: nowrap; }
  .socials__badge { width: 27px; height: 27px; border: 1.5px solid var(--white); border-radius: 50%; flex: none; }
</style>
</head>
<body>

<section class="card card--front" aria-label="Card front">
  <div class="brand">
    <span class="brand__mark" aria-hidden="true"></span>
    <div class="brand__name">Fernwick Grove</div>
    <div class="brand__tagline">SUPPLEMENTS • HEALTH FOODS • REMEDIES</div>
  </div>

  <div class="divider" aria-hidden="true"></div>

  <div class="contact">
    <p class="contact__address">2417 Larkwood Ave.<br>Calloway Springs, CA 95871<br>(corner of Dunmore St.)</p>
    <ul class="contact__list">
      <li class="contact__item">
        <svg class="contact__icon" viewBox="0 0 24 24" aria-hidden="true"><path fill="#4db749" d="M6.6 10.8a15.1 15.1 0 0 0 6.6 6.6l2.2-2.2a1 1 0 0 1 1-.25 11.4 11.4 0 0 0 3.6.57 1 1 0 0 1 1 1V20a1 1 0 0 1-1 1A17 17 0 0 1 3 4a1 1 0 0 1 1-1h3.5a1 1 0 0 1 1 1c0 1.25.2 2.45.57 3.57a1 1 0 0 1-.25 1z"/></svg>
        707-314-2296
      </li>
      <li class="contact__item">
        <svg class="contact__icon" viewBox="0 0 24 24" aria-hidden="true"><rect x="2" y="5" width="20" height="14" rx="1.5" fill="#4db749"/><path d="M2.5 6 12 13l9.5-7" fill="none" stroke="#fff" stroke-width="1.6"/></svg>
        FernwickLiving@mailbox.example
      </li>
      <li class="contact__item">
        <svg class="contact__icon" viewBox="0 0 24 24" aria-hidden="true"><circle cx="12" cy="12" r="10" fill="#4db749"/><path d="M2 12h20M12 2c3 3 3 17 0 20M12 2c-3 3-3 17 0 20" fill="none" stroke="#fff" stroke-width="1.4"/></svg>
        www.FernwickGrove.example
      </li>
    </ul>
  </div>

  <div class="seal" role="img" aria-label="Celebrating 25 years, 1997 to 2022">
    <span class="seal__label">CELEBRATING</span>
    <span class="seal__number">25</span>
    <span class="seal__unit">YEARS</span>
    <span class="seal__dates">1997 – 2022</span>
  </div>
</section>

<section class="card card--back" aria-label="Card back">
  <div class="brand">
    <span class="brand__mark" aria-hidden="true"></span>
    <div class="brand__name">Fernwick Grove</div>
    <div class="brand__tagline">SUPPLEMENTS • HEALTH FOODS • REMEDIES</div>
  </div>

  <ul class="socials">
    <li class="socials__item"><span class="socials__badge" aria-hidden="true"></span>FernwickGroveShop</li>
    <li class="socials__item"><span class="socials__badge" aria-hidden="true"></span>FernwickGroveShop</li>
    <li class="socials__item"><span class="socials__badge" aria-hidden="true"></span>VisitFernwickGrove</li>
  </ul>
</section>

</body>
</html>
```